Vora Dishwasher Pods (Pack design) *

We require a doy pack design for a new dishwasher pod brand. It aims at competing with the top tier global brands, and hence needs to have 'big brand feel'. The product is of high quality, slightly lower priced and hence makes "Vora" for the consumer to purchase.

The design should be clean, sophisticated, modern, and appeal to the upper end consumer.

What's important, is that the consumer is habitually buying the known-brand, and hence we need to quickly and visually establish what the product is (dishwashing tablet) and also establish trust (the product will deliver). Hence we can borrow equity from category cues (see design brief)

Target Market(s)

Upper LSM (mid to higher end of the market). Dishwasher penetration is low, and hence only the top end of the market has a dishwasher

Industry/Entity Type

Cleaning Product

Font styles to use
Sans Serif

Colors
ffffff
000000
0255a3
33a6d7
fbee3d
add136

Requirements
Must have
• Message/Idea/Visual Hierarchy:
• Priority 1: Category / Product Type (i.e. "Dishwasher Pods"). Category most important, then the brand name. Could be joined. This must be clear, and stand out!
• Priority 2: Efficient cleaning pod/tablet which cleans thoroughly (scienctific cues, sparkles, foam, lemon/lime, etc.). Please use 3D art, rather than flat artwork. The idea that we may be well priced, but the technology is state-of-the-art. People are taking a risk buying us, so we need to comfort them that the product will work! We need to establish brand trust with our serious and professional look.
• Priority 3: Stand-out, bold, clean, modern, simple design. Simple doesn't mean "no class and style". Competitors have busy packaging with lots of colours and text.
• Lastly: We are "sensible" (in terms of cost and efficiency), "conscious", "have values". We may partner with a "Save Water" organisation. Hence the feeling of "values" and the "human touch" is a nice-to-have. We may be serious in packaging, but we care about you, your pocket, society and the environment. Hence you can contact us on plonkit for instant-chat (see packagaing text).
Nice to have
• - A simple placeholder 'back of pack' text "Lorem ipsum". No need for excessive design, this will be worked upon in Round 2 with the winning design(er).
• - In a world where clean modern and computers dominate, there can be perfection in imperfection. There can be a personal (human) touch added. Think detailed droplets, or 3D/natural feel.
• - Dummy barcode
• - As for the colours, we are very open to ideas and the given colours in the project was only a guideline. Don't necessarily stick to them - we encourage creativity.
Should not have
• The brand is not:
• - Cheap and cheesy and cartoonish (as most competitors). Instead we are 3D, real!
• - Busy and tiring on the eye (as the lead competitor). It can be bold, stylish, eye-catching, but not overly busy and dainty. Think of Brimlo (infancy days) vs Zelta (market leader days).

```html
<!DOCTYPE html>
<html lang="en">
<head>
<meta charset="utf-8">
<title>Vora Dishwasher Pods – Pack Front</title>
<link rel="stylesheet" href="https://fonts.googleapis.com/css2?family=Fira+Sans:ital,wght@0,400;0,600;0,800;1,400;1,600&family=Fira+Sans+Condensed:wght@600&display=swap">
<style>
  :root {
    --lime: #dfe87c;
    --lime-deep: #c9d85a;
    --lime-text: #e3ec86;
    --ink: #161613;
    --white: #ffffff;
    --pod-blue: #4f7fc9;
    --pod-yellow: #e8d44a;
    --grey-light: #f2f2ef;
    --grey-mid: #c9cbc5;
  }
  * { margin: 0; padding: 0; box-sizing: border-box; }
  html, body {
    width: 1200px; height: 1200px; overflow: hidden;
    background: var(--white);
    font-family: "Fira Sans", sans-serif;
  }
  .pack {
    position: absolute; left: 288px; top: 142px;
    width: 618px; height: 930px;
    background: linear-gradient(180deg, var(--lime) 0%, #e4ec88 60%, var(--lime-deep) 100%);
    border-radius: 10px 10px 4px 4px;
    overflow: hidden;
  }
  .tear-notch {
    position: absolute; top: 112px; width: 18px; height: 18px;
    background: var(--white); border-radius: 50%;
  }
  .tear-notch.left { left: -9px; }
  .tear-notch.right { right: -9px; }
  .pattern-area {
    position: absolute; left: 0; top: 60px; width: 300px; height: 240px;
    background: radial-gradient(ellipse at 50% 50%, rgba(190,205,70,0.55), rgba(223,232,124,0) 70%);
  }
  .brand-block {
    position: absolute; right: 0; top: 0; width: 330px; height: 202px;
    background: var(--ink);
  }
  .tear-note {
    position: absolute; left: 38px; top: 34px;
    font-family: "Fira Sans Condensed", sans-serif; font-weight: 600;
    font-size: 10px; letter-spacing: 0.3px; color: var(--white);
  }
  .brand-name {
    position: absolute; left: 34px; top: 118px;
    font-weight: 400; font-size: 50px; letter-spacing: 1px; line-height: 1;
    color: var(--lime-text);
  }
  .dishes-photo {
    position: absolute; left: 0; top: 250px; width: 560px; height: 470px;
    background: radial-gradient(ellipse at 35% 55%, var(--white) 0%, var(--grey-light) 40%, var(--grey-mid) 75%, rgba(201,203,197,0) 100%);
  }
  .headline {
    position: absolute; left: 322px; top: 216px;
    font-weight: 800; font-size: 46px; line-height: 1.1; color: var(--ink);
    z-index: 2;
  }
  .pod-visual {
    position: absolute; left: 442px; top: 266px; width: 146px; height: 98px;
    border-radius: 14px;
    background: linear-gradient(160deg, #6b95d6 0%, var(--pod-blue) 70%, #e9e9e6 100%);
    transform: rotate(-6deg);
    z-index: 1;
  }
  .pod-visual::after {
    content: ""; position: absolute; left: 40px; top: 14px; width: 52px; height: 44px;
    border-radius: 8px; background: var(--pod-yellow);
  }
  .claims { position: absolute; left: 299px; top: 400px; width: 319px; list-style: none; }
  .claim {
    height: 44px; margin-bottom: 6px;
    background: var(--ink); color: var(--white);
    font-style: italic; font-size: 18px;
    display: flex; align-items: center; padding-left: 24px;
    transform: skewY(-1.5deg);
  }
  .base-band { position: absolute; left: 0; top: 660px; width: 618px; height: 270px; }
  .base-pattern {
    position: absolute; left: 16px; top: 700px; width: 360px; height: 110px;
    background: radial-gradient(ellipse at 40% 50%, rgba(120,135,40,0.6), rgba(22,22,19,0) 70%);
  }
  .count {
    position: absolute; left: 46px; top: 834px;
    font-style: italic; font-weight: 600; font-size: 26px; color: var(--lime-text);
    transform: rotate(5deg);
  }
  .weight {
    position: absolute; left: 170px; top: 872px;
    font-style: italic; font-size: 19px; color: var(--lime-text);
    transform: rotate(2deg);
  }
  .partner { position: absolute; left: 440px; top: 750px; text-align: center; width: 130px; }
  .partner-mark, .chat-mark {
    display: block; margin: 0 auto; width: 30px; height: 30px; background: var(--white);
  }
  .partner-name {
    display: block; margin-top: 8px;
    font-size: 14px; letter-spacing: 3px; color: var(--white);
  }
  .chat { position: absolute; left: 390px; top: 824px; width: 230px; text-align: center; }
  .chat-mark { width: 34px; height: 34px; border-radius: 6px; }
  .chat-name {
    display: block; margin-top: 4px; font-size: 13px; color: var(--white);
  }
  .chat-handle {
    display: block; margin-top: 4px; font-size: 12px; color: var(--white);
    transform: rotate(-5deg);
  }
</style>
</head>
<body>
<main class="pack">
  <div class="pattern-area" role="img" aria-label="Soft lime hexagon molecule pattern"></div>
  <div class="dishes-photo" role="img" aria-label="Photo of sparkling clean white cups, plates and cutlery"></div>

  <section class="brand-block">
    <p class="tear-note">TEAR OPEN HERE. RESEAL AFTER USE.</p>
    <p class="brand-name">vora</p>
  </section>

  <h1 class="headline">Dishwasher<br>Pods</h1>
  <div class="pod-visual" role="img" aria-label="3D dishwasher pod tablet, blue with yellow centre"></div>

  <ul class="claims">
    <li class="claim">Easily removes tough food stains</li>
    <li class="claim">Clears away residue</li>
    <li class="claim">Dissolvable wrapping</li>
  </ul>

  <svg class="base-band" viewBox="0 0 618 270" preserveAspectRatio="none" aria-hidden="true">
    <path d="M0 30 C 150 28, 220 80, 330 78 C 430 76, 520 40, 618 36 L618 270 L0 270 Z" fill="#161613"/>
  </svg>
  <div class="base-pattern" role="img" aria-label="Hexagon molecule pattern in olive and white"></div>

  <p class="count">44 pods</p>
  <p class="weight">weight: 123 g</p>

  <div class="partner">
    <span class="partner-mark"></span>
    <span class="partner-name">clearwell</span>
  </div>

  <div class="chat">
    <span class="chat-mark"></span>
    <span class="chat-name">plonkit</span>
    <span class="chat-handle">@VoraCleanseSA Let’s chat</span>
  </div>

  <span class="tear-notch left"></span>
  <span class="tear-notch right"></span>
</main>
</body>
</html>
```